" Abrimos o escritório há poucos meses. Somos duas mulheres, a Sofia recém formada e a Berta formada há pouco mais de quatro anos. Estamos iniciando nossa carreira como advogadas esse ano, por enquanto, trabalhamos nós duas atuando nas mais diversas áreas do direito, sobretudo, cível, previdenciário e criminal. "

```html
<!DOCTYPE html>
<html lang="pt-BR">
<head>
<meta charset="UTF-8">
<title>Valverde &amp; Rocha Advocacia — Pasta institucional</title>
<link rel="stylesheet" href="https://fonts.googleapis.com/css2?family=Cinzel:wght@400&family=Roboto:wght@400&display=swap">
<style>
  :root {
    --backdrop: #efece8;
    --burgundy: #6a1a33;
    --burgundy-deep: #5a1429;
    --burgundy-flap: #651830;
    --gold: #c9a36c;
    --text-light: #f1e6e9;
  }
  * { margin: 0; padding: 0; box-sizing: border-box; }
  html, body {
    width: 1200px; height: 1200px; overflow: hidden;
    background: var(--backdrop);
  }
  .canvas { position: relative; width: 1200px; height: 1200px; }

  .folder-flap { position: absolute; left: 240px; top: 790px; width: 420px; height: 250px; }

  .folder {
    position: absolute; left: 240px; top: 211px; width: 732px; height: 593px;
    display: flex;
    box-shadow: 0 6px 18px rgba(0,0,0,0.18);
  }
  .panel { position: relative; height: 100%; background: var(--burgundy); }
  .panel--back { width: 389px; }
  .panel--front { width: 343px; border-left: 1px solid var(--burgundy-deep); }
  .gold-rule {
    position: absolute; left: 0; right: 0; bottom: 12px; height: 3px;
    background: linear-gradient(90deg, #a97b45, var(--gold), #e3c697, var(--gold));
  }

  .brand-name {
    font-family: "Cinzel", serif; font-weight: 400; color: var(--gold);
    letter-spacing: 0.04em; white-space: nowrap;
  }
  .brand-mark { display: inline-block; background: var(--gold); }

  .front-brand {
    position: absolute; left: 0; right: 0; top: 220px; text-align: center;
  }
  .front-brand .brand-mark { width: 26px; height: 26px; margin-bottom: 22px; }
  .front-brand .brand-name { display: block; font-size: 27px; }
  .front-brand .brand-tagline {
    display: block; margin-top: 8px; font-size: 12px; letter-spacing: 0.55em;
  }

  .back-contact {
    position: absolute; left: 0; right: 0; top: 480px; text-align: center;
    font-family: "Roboto", sans-serif; color: var(--text-light);
  }
  .back-contact .brand-name { display: block; font-size: 13px; margin-bottom: 16px; }
  .contact-line { font-size: 9.5px; line-height: 14px; white-space: nowrap; }
  .contact-line span + span { margin-left: 18px; }

  .website {
    position: absolute; right: 36px; bottom: 27px;
    font-family: "Roboto", sans-serif; font-size: 10px; color: var(--text-light);
  }
</style>
</head>
<body>
<main class="canvas">
  <svg class="folder-flap" viewBox="0 0 420 250" aria-hidden="true">
    <path d="M12 14 H390 C412 14 418 70 404 140 C392 205 340 238 270 238 H150 C120 238 100 222 88 200 V60 L12 44 Z" fill="var(--burgundy-flap)"/>
    <path d="M12 14 H88 V200 C70 190 40 190 12 194 Z" fill="var(--burgundy-deep)"/>
  </svg>

  <section class="folder">
    <div class="panel panel--back">
      <div class="back-contact">
        <span class="brand-name">Valverde &amp; Rocha</span>
        <p class="contact-line">contato@valverderocha.adv.br</p>
        <p class="contact-line"><span>(00) 0000-0000</span><span>(00) 00000-0000</span></p>
        <p class="contact-line">Rua Dr. Augusto Ferraz de Melo nº45 - Lapa - São Paulo - SP - 05041-020</p>
      </div>
      <div class="gold-rule"></div>
    </div>
    <div class="panel panel--front">
      <div class="front-brand">
        <span class="brand-mark"></span>
        <span class="brand-name">Valverde &amp; Rocha</span>
        <span class="brand-name brand-tagline">Advocacia</span>
      </div>
      <p class="website">www.valverderocha.adv.br</p>
      <div class="gold-rule"></div>
    </div>
  </section>
</main>
</body>
</html>
```